Modern Business Card for Lanternfield 2018

Our company assumes the best about people. We are creating an online community of entrepreneurs and business leaders who struggle with marketing their business online.

This business card should POP! We recently got a new logo and are launching a new website next month, so our business cards should make a statement that feels:
-Fresh
-Smart
-Trustworthy
-Fun

Target Market(s)

small business owners, entrepreneurs

Industry/Entity Type

Digital Marketing

Contact Information for Business Card

Dimensions: 3.5" x 2"

Font styles to use
Sans Serif

Colors
f37122
ffffff

Requirements
Must have
• We need a business card with a modern, bold design. We will use one side of the card as a lead-generation offer, so text on one side will need to fit up to 140 characters. The business card should stick to our core colors (orange, black, and white).
Nice to have
• We think a vertical "portrait" design could be interesting.
Should not have
• Should not look like a traditional business card. The round icon should stand out from a distance.

```html
<!DOCTYPE html>
<html lang="en">
<head>
<meta charset="utf-8">
<title>Lanternfield Business Card</title>
<link href="https://fonts.googleapis.com/css2?family=Montserrat:wght@400;500;700&display=swap" rel="stylesheet">
<style>
  :root {
    --orange: #f37122;
    --black: #1e1e1e;
    --white: #ffffff;
    --paper: #f7f7f5;
    --peach: #f6d3c4;
    --backdrop: #e4e4e2;
    --ink: #2a2a2a;
  }
  * { margin: 0; padding: 0; box-sizing: border-box; }
  html, body { width: 1200px; height: 800px; overflow: hidden; }
  body {
    background: var(--backdrop);
    font-family: "Montserrat", sans-serif;
    display: flex;
    align-items: center;
    justify-content: center;
    gap: 60px;
  }
  .card {
    position: relative;
    width: 525px;
    height: 300px;
    background: var(--paper);
    overflow: hidden;
    box-shadow: 0 6px 18px rgba(0,0,0,0.12);
  }

  /* Brand lockup */
  .brand { position: absolute; display: flex; align-items: center; gap: 10px; }
  .brand-dot { width: 44px; height: 44px; border-radius: 50%; background: var(--orange); flex: none; }
  .brand-text { display: flex; flex-direction: column; }
  .brand-name { color: var(--orange); font-weight: 700; font-size: 24px; letter-spacing: 0.5px; line-height: 1; text-transform: uppercase; }
  .brand-tagline { color: var(--ink); font-size: 8px; margin-top: 4px; letter-spacing: 0.3px; }

  /* Front */
  .front-decor { position: absolute; right: 0; top: 95px; width: 250px; height: 170px; background: var(--peach); }
  .front-band { position: absolute; left: 0; top: 0; width: 100%; height: 95px; background: var(--black); }
  .person { position: absolute; left: 34px; top: 30px; }
  .person-name { color: var(--orange); font-weight: 500; font-size: 21px; font-variant: small-caps; letter-spacing: 1px; line-height: 1; }
  .person-role { color: var(--white); font-size: 11px; margin-top: 6px; letter-spacing: 0.5px; }
  .front .brand { right: 36px; top: 64px; flex-direction: column; gap: 8px; }
  .front .brand-text { align-items: center; }
  .front .brand-name { font-size: 22px; }
  .front .brand-dot { width: 58px; height: 58px; border: 5px solid var(--paper); }
  .contact-list { position: absolute; left: 34px; bottom: 58px; list-style: none; }
  .contact-list li { display: flex; align-items: center; gap: 8px; font-size: 11.5px; color: var(--ink); letter-spacing: 0.6px; margin-top: 6px; }
  .contact-icon { width: 15px; height: 15px; flex: none; }
  .front-stripe { position: absolute; left: 0; bottom: 30px; width: 100%; height: 8px; background: var(--orange); }

  /* Back */
  .back .brand { left: 150px; top: 42px; }
  .offer { position: absolute; left: 40px; top: 110px; width: 445px; font-size: 11.5px; color: var(--ink); line-height: 1.6; letter-spacing: 0.4px; text-align: center; }
  .write-lines { position: absolute; left: 150px; top: 160px; width: 300px; }
  .write-lines span { display: block; border-bottom: 1px dotted #777; height: 20px; }
  .back-stripe { position: absolute; left: 0; bottom: 60px; width: 100%; height: 6px; background: var(--orange); }
  .back-band { position: absolute; left: 0; bottom: 0; width: 100%; height: 60px; background: var(--black); display: flex; align-items: center; justify-content: center; }
  .website { color: var(--white); font-size: 15px; letter-spacing: 3px; }
  .website em { font-style: normal; color: var(--orange); }
</style>
</head>
<body>
  <article class="card front">
    <div class="front-decor" role="img" aria-label="Soft peach decorative area"></div>
    <div class="front-band"></div>
    <div class="person">
      <div class="person-name">Miles Dorran</div>
      <div class="person-role">Founder &amp; CEO</div>
    </div>
    <div class="brand">
      <span class="brand-dot"></span>
      <div class="brand-text">
        <span class="brand-name">Lanternfield</span>
        <span class="brand-tagline">ideas that move people forward</span>
      </div>
    </div>
    <ul class="contact-list">
      <li>
        <svg class="contact-icon" viewBox="0 0 16 16"><circle cx="8" cy="8" r="8" fill="#1e1e1e"/><path d="M5.3 4.5l1.3 1.6-.7.9c.5 1 1.2 1.7 2.2 2.2l.9-.7 1.6 1.3-.9 1.3C7.7 10.8 5.2 8.3 4.9 6.3z" fill="#fff"/></svg>
        000.000.0000
      </li>
      <li>
        <svg class="contact-icon" viewBox="0 0 16 16"><circle cx="8" cy="8" r="8" fill="#1e1e1e"/><path d="M4 8l8-3.5-2.5 8-2-3z" fill="#fff"/></svg>
        miles@lanternfieldhub.com
      </li>
      <li>
        <svg class="contact-icon" viewBox="0 0 16 16"><circle cx="8" cy="8" r="8" fill="#1e1e1e"/><path d="M5 5l6 2.4-2.4 1.2L7.4 11z" fill="#fff"/></svg>
        www.lanternfieldhub.com
      </li>
    </ul>
    <div class="front-stripe"></div>
  </article>

  <article class="card back">
    <div class="brand">
      <span class="brand-dot"></span>
      <div class="brand-text">
        <span class="brand-name">Lanternfield</span>
        <span class="brand-tagline">ideas that move people forward</span>
      </div>
    </div>
    <p class="offer">Lorem Ipsum is simply dummy text of the printing and typesetting industry. Lorem Ipsum has been the industry's standard dummy text ever since.</p>
    <div class="write-lines"><span></span><span></span><span></span></div>
    <div class="back-stripe"></div>
    <div class="back-band">
      <span class="website">www.<em>lanternfieldhub</em>.com</span>
    </div>
  </article>
</body>
</html>
```